International professional tennis coach needs a book cover design

This is my 2nd published book, the first one was a #1 on the best seller. I'm looking for a world class book cover design for this new book. The name of my first book was 5 Baseline Habits to Unlock Your Rally Rhythm, located on Brimlow.com

The title of the new book:

Title: The Craft of Steady Rallies
Subtitle: Building a Tactical Margin by Way of Opponent Insight

I'm uploading our new CRAFT OF STEADY logo that I'd like for you to use as the centerpiece of the book design along with a 21st century design feel that incorporates what the book topic is below::

--> This book is about building competitive intelligence by using tennis data analytics to develop and expand a player's strategic advantage for match play. <--

The colors we would like to use are Blue, Yellow, and Green. These shades of these colors should be bold! (You will see the bold color examples of blues, yellows, and greens that I'm talking about in the logos that are attached here, especially the colors for my Tennis GridRally App logo.

I will upload the Tennis GridRally logo which should go somewhere on the back cover design (small size maybe in the bottom corner).

This book is revolutionary to the standard way of teaching tennis, it is based on a decade of recording and gathering tennis data analytics and then we created on-court practice games to develop better decision making in players for the competitive edge.

My websites are www.elevatedrillzone.com and www.craftofsteadyrallies.com

```html
<!DOCTYPE html>
<html lang="en">
<head>
<meta charset="utf-8">
<title>The Craft of Steady Rallies — Book Cover</title>
<link href="https://fonts.googleapis.com/css2?family=Great+Vibes&family=Playfair+Display:wght@400;700&family=Oswald:wght@500&display=swap" rel="stylesheet">
<style>
  :root {
    --stage: #d6d6d6;
    --cover: #ffffff;
    --cover-shade: #e6e6e6;
    --green-deep: #136510;
    --green-title: #1b6e14;
    --green-light: #7db443;
    --blue: #0a5fe0;
    --text-dark: #1d1d1d;
  }
  * { margin: 0; padding: 0; box-sizing: border-box; }
  html, body {
    width: 1200px;
    height: 1200px;
    overflow: hidden;
    background: var(--stage);
  }
  .canvas {
    position: relative;
    width: 1200px;
    height: 1200px;
    display: flex;
    align-items: center;
    justify-content: center;
  }
  .cover {
    position: relative;
    width: 734px;
    height: 1100px;
    background: linear-gradient(90deg, var(--cover) 0%, var(--cover-shade) 50%, var(--cover) 100%);
    text-align: center;
  }
  .title-script {
    position: absolute;
    top: 70px;
    left: 0;
    right: 0;
    font-family: "Great Vibes", cursive;
    font-size: 74px;
    line-height: 1;
    color: var(--green-light);
  }
  .title-main {
    position: absolute;
    top: 150px;
    left: 0;
    right: 0;
    font-family: "Playfair Display", serif;
    font-weight: 700;
    color: var(--green-title);
    line-height: 1;
  }
  .title-main span { display: block; }
  .title-main .line-one { font-size: 136px; letter-spacing: 2px; }
  .title-main .line-two { font-size: 136px; margin-top: -4px; letter-spacing: 2px; }
  .brand-mark {
    position: absolute;
    top: 560px;
    left: 0;
    right: 0;
    display: flex;
    align-items: center;
    justify-content: center;
    gap: 16px;
    font-family: "Oswald", sans-serif;
    font-weight: 500;
    font-size: 50px;
    letter-spacing: 2px;
    color: var(--blue);
  }
  .brand-dot {
    width: 34px;
    height: 34px;
    border-radius: 50%;
    background: var(--blue);
  }
  .rule {
    position: absolute;
    left: 143px;
    width: 448px;
    height: 1px;
    background: linear-gradient(90deg, transparent, var(--green-light) 15%, var(--green-light) 85%, transparent);
  }
  .rule.top { top: 790px; }
  .rule.bottom { top: 888px; }
  .subtitle {
    position: absolute;
    top: 800px;
    left: 0;
    right: 0;
    font-family: "Playfair Display", serif;
    font-weight: 400;
    font-size: 30px;
    line-height: 38px;
    letter-spacing: 1.5px;
    color: var(--text-dark);
  }
  .authors {
    position: absolute;
    top: 982px;
    left: 0;
    right: 0;
    font-family: "Oswald", sans-serif;
    font-weight: 500;
    font-size: 44px;
    line-height: 1;
    color: var(--green-deep);
  }
</style>
</head>
<body>
  <main class="canvas">
    <section class="cover">
      <div class="title-script">The Craft of</div>
      <h1 class="title-main">
        <span class="line-one">STEADY</span>
        <span class="line-two">RALLIES</span>
      </h1>
      <div class="brand-mark">
        <span class="brand-dot"></span>
        <span class="brand-name">CRAFT OF STEADY</span>
      </div>
      <div class="rule top"></div>
      <p class="subtitle">Building a Tactical Margin<br>by Way of Opponent Insight</p>
      <div class="rule bottom"></div>
      <p class="authors">CORWIN ASHDALE &amp; MARA PELLSTON</p>
    </section>
  </main>
</body>
</html>
```